Solace Chiropractic & Acupuncture Business Cards

I need a business card design that feels elevated. I am open to any of the logo designs uploaded. We have two doctors so I'll need to be able to change out the names.

Information:
Marnie Toller D.C., Dipl. Ac. ASA
584 W 12th St, Ste 320
Larkfield, NE 67419
solacegrove.net
620-555-0147
drmarnie@solacegrove.com
Updates

We have designs we like now, we are just trying to choose between top contenders. Thanks for your submissions!

Contact Information for Business Card

noted in description

Requirements
Must have
• ability to edit info if possible
Nice to have
• Please see our website solacegrove.net for our style and colors

```html
<!DOCTYPE html>
<html lang="en">
<head>
<meta charset="utf-8">
<title>Solace Chiropractic &amp; Acupuncture — Business Cards</title>
<link rel="stylesheet" href="https://fonts.googleapis.com/css2?family=Open+Sans:wght@300;400&family=Playfair+Display:wght@400&display=swap">
<style>
  :root {
    --page: #ffffff;
    --card-front: #e8e5de;
    --card-back: #cdc3b6;
    --ink: #2f3448;
    --ink-soft: #3d4256;
    --rule: #5b5f6e;
    --shadow: rgba(0, 0, 0, 0.22);
  }
  * { margin: 0; padding: 0; box-sizing: border-box; }
  html, body {
    width: 1200px; height: 1000px; overflow: hidden;
    background: var(--page);
  }
  .sheet { position: relative; width: 1200px; height: 1000px; }

  .card {
    position: absolute;
    box-shadow: 2px 4px 10px var(--shadow);
  }
  .card--front {
    left: 281px; top: 105px; width: 638px; height: 360px;
    background: var(--card-front);
  }
  .card--back {
    left: 282px; top: 506px; width: 638px; height: 357px;
    background: var(--card-back);
  }

  /* Front: brand name */
  .brand-name {
    position: absolute; left: 0; right: 0; top: 118px;
    text-align: center;
    font-family: "Playfair Display", serif;
    font-weight: 400;
    color: var(--ink);
  }
  .brand-name__main {
    display: block;
    font-size: 104px; line-height: 1;
    letter-spacing: -1px;
  }
  .brand-name__sub {
    display: block;
    margin-top: 4px; margin-left: 76px;
    font-size: 14px; letter-spacing: 0.4px;
    text-transform: uppercase;
  }

  /* Back: seal */
  .seal {
    position: absolute; left: 51px; top: 68px;
    width: 178px; height: 218px;
    border: 1.5px solid var(--ink);
    border-radius: 50%;
    display: flex; align-items: center; justify-content: center;
    font-family: "Playfair Display", serif;
    font-weight: 400; font-size: 34px;
    color: var(--ink);
  }

  .divider {
    position: absolute; left: 265px; top: 43px;
    width: 1px; height: 272px; background: var(--rule);
  }

  .doctor {
    position: absolute; left: 290px; top: 52px;
    color: var(--ink);
  }
  .doctor__name {
    font-family: "Playfair Display", serif;
    font-weight: 400; font-size: 39px; line-height: 1.1;
  }
  .doctor__credentials {
    margin-top: 4px;
    font-family: "Open Sans", sans-serif;
    font-weight: 300; font-size: 20px;
    color: var(--ink);
  }
  .doctor__rule {
    margin-top: 14px; width: 62px; height: 1px; background: var(--rule);
  }

  .contact { position: absolute; left: 288px; list-style: none; }
  .contact__item {
    position: absolute; left: 0;
    display: flex; align-items: center;
    font-family: "Open Sans", sans-serif;
    font-weight: 400; font-size: 14px; line-height: 18px;
    letter-spacing: 0.4px;
    color: var(--ink-soft);
    white-space: nowrap;
  }
  .contact__icon {
    width: 24px; height: 24px; margin-right: 14px; flex: none;
    fill: none; stroke: var(--ink-soft); stroke-width: 1.3;
    stroke-linecap: round; stroke-linejoin: round;
  }
  .contact__item--address { top: 159px; }
  .contact__item--web { top: 210px; }
  .contact__item--phone { top: 260px; }
  .contact__item--email { top: 298px; }
</style>
</head>
<body>
<main class="sheet">

  <section class="card card--front" aria-label="Business card front">
    <h1 class="brand-name">
      <span class="brand-name__main">Solace</span>
      <span class="brand-name__sub">Chiropractic &amp; Acupuncture</span>
    </h1>
  </section>

  <section class="card card--back" aria-label="Business card back">
    <div class="seal">Solace</div>
    <div class="divider"></div>

    <div class="doctor">
      <h2 class="doctor__name">Dr. Marnie Toller</h2>
      <p class="doctor__credentials">D.C., Dipl. Ac. ASA</p>
      <div class="doctor__rule"></div>
    </div>

    <ul class="contact">
      <li class="contact__item contact__item--address">
        <svg class="contact__icon" viewBox="0 0 24 24" aria-hidden="true">
          <path d="M12 22s-7-7.2-7-12.2A7 7 0 0 1 19 9.8C19 14.8 12 22 12 22z"/>
          <circle cx="12" cy="10" r="2.6"/>
        </svg>
        <span>584 W 12th St, Ste 320<br>Larkfield, NE 67419</span>
      </li>
      <li class="contact__item contact__item--web">
        <svg class="contact__icon" viewBox="0 0 24 24" aria-hidden="true">
          <circle cx="12" cy="12" r="10"/>
          <ellipse cx="12" cy="12" rx="4.2" ry="10"/>
          <path d="M2 12h20M3.5 7h17M3.5 17h17"/>
        </svg>
        <span>solacegrove.net</span>
      </li>
      <li class="contact__item contact__item--phone">
        <svg class="contact__icon" viewBox="0 0 24 24" aria-hidden="true">
          <path d="M5 2.5h3.5l1.8 4.6-2.3 1.6a12 12 0 0 0 6.3 6.3l1.6-2.3 4.6 1.8V18a2.5 2.5 0 0 1-2.7 2.5C10 20 4 14 3.5 5.2A2.5 2.5 0 0 1 5 2.5z"/>
        </svg>
        <span>620-555-0147</span>
      </li>
      <li class="contact__item contact__item--email">
        <svg class="contact__icon" viewBox="0 0 24 24" aria-hidden="true">
          <rect x="2" y="5" width="20" height="14"/>
          <path d="M2 5l10 8 10-8M2 19l7.5-7M22 19l-7.5-7"/>
        </svg>
        <span>drmarnie@solacegrove.com</span>
      </li>
    </ul>
  </section>

</main>
</body>
</html>
```